Business Card Design

We are looking for a double sided business card.

On one side would be our logo

On the Other Side

Daniel Workby
Sales and Marketing

Phone/Text Logo and 530-471-6328
Email Logo and info@gildedcritters.example
Website Logo and www.gildedcritters.example
Facebook Logo and gilded critters
Instagram Logo and gilded_critters

Target Market(s)

Pet owners

Contact Information for Business Card

In project description

Requirements
Must have
• Logo

```html
<!DOCTYPE html>
<html lang="en">
<head>
<meta charset="utf-8">
<title>Gilded Critters – Business Card</title>
<link href="https://fonts.googleapis.com/css2?family=Montserrat:wght@400;500;600&display=swap" rel="stylesheet">
<style>
  :root {
    --backdrop: #2c2c2c;
    --card: #000000;
    --orange: #f07f22;
    --amber: #f6b21f;
    --silver: #d9d9d9;
    --white: #ffffff;
  }
  * { margin: 0; padding: 0; box-sizing: border-box; }
  html, body { width: 1200px; height: 1015px; overflow: hidden; background: var(--backdrop); }
  body { font-family: "Montserrat", sans-serif; color: var(--white); position: relative; }

  .card {
    position: absolute; left: 250px; width: 700px; height: 400px;
    background: var(--card); overflow: hidden;
    box-shadow: 0 10px 30px rgba(0,0,0,.45);
  }
  .card-front { top: 60px; }
  .card-back { top: 535px; }

  .helix-band { position: absolute; left: 0; bottom: 0; width: 700px; height: 60px; }

  .front-brand {
    position: absolute; top: 110px; left: 0; width: 100%; text-align: center;
  }
  .front-brand .brand-name {
    font-weight: 600; font-size: 62px; letter-spacing: 2px; color: var(--silver);
    text-transform: uppercase; line-height: 1;
  }
  .front-brand .brand-site {
    margin-top: 22px; font-size: 13px; letter-spacing: 6px; color: var(--amber);
    text-transform: uppercase; font-weight: 500;
  }

  .back-brand {
    position: absolute; top: 60px; right: 50px; display: flex; align-items: center; gap: 12px;
  }
  .back-brand .brand-dot { width: 18px; height: 18px; border-radius: 50%; background: var(--orange); }
  .back-brand .brand-name {
    font-weight: 600; font-size: 36px; color: var(--orange); text-transform: uppercase; letter-spacing: 1px;
  }

  .identity { position: absolute; top: 135px; left: 30px; display: flex; gap: 16px; }
  .identity .accent-bar { width: 10px; height: 48px; background: linear-gradient(var(--amber), var(--orange)); }
  .identity .person-name {
    font-size: 24px; font-weight: 500; color: var(--orange); text-transform: uppercase; line-height: 1.1;
  }
  .identity .person-role { font-size: 19px; color: var(--white); }

  .contact-list { position: absolute; left: 110px; list-style: none; font-size: 18px; }
  .contact-social { top: 205px; }
  .contact-direct { top: 265px; }
  .contact-list li { display: flex; align-items: center; gap: 10px; height: 24px; }
  .contact-list svg { width: 16px; height: 16px; flex: none; }
  .social-square { width: 12px; height: 12px; background: var(--orange); margin: 0 2px; flex: none; }
  .web-domain { color: var(--orange); }
</style>
</head>
<body>

<svg width="0" height="0" style="position:absolute">
  <defs>
    <linearGradient id="bandGradient" x1="0" x2="1" y1="0" y2="0">
      <stop offset="0" stop-color="#f6b21f"/>
      <stop offset=".5" stop-color="#f07f22"/>
      <stop offset="1" stop-color="#f6b21f"/>
    </linearGradient>
  </defs>
</svg>

<section class="card card-front">
  <div class="front-brand">
    <div class="brand-name">Gilded Critters</div>
    <div class="brand-site">www.gildedcritters.example</div>
  </div>
  <svg class="helix-band" viewBox="0 0 700 60" role="img" aria-label="Decorative double-helix strand in gold, orange and silver along the bottom edge">
    <path d="M0 60 L0 56 C120 36 230 50 350 42 C470 34 580 42 700 12 L700 60 Z" fill="url(#bandGradient)"/>
  </svg>
</section>

<section class="card card-back">
  <div class="back-brand">
    <span class="brand-dot"></span>
    <span class="brand-name">Gilded Critters</span>
  </div>

  <div class="identity">
    <span class="accent-bar"></span>
    <div>
      <div class="person-name">Daniel Workby</div>
      <div class="person-role">Sales and Marketing</div>
    </div>
  </div>

  <ul class="contact-list contact-social">
    <li><span class="social-square"></span>gilded critters</li>
    <li><span class="social-square"></span>gilded_critters</li>
  </ul>

  <ul class="contact-list contact-direct">
    <li>
      <svg viewBox="0 0 16 16" aria-hidden="true"><path d="M3 1 L6 1 L7 5 L5 6.5 C6 9 7 10 9.5 11 L11 9 L15 10 L15 13 C15 14 14 15 13 15 C6 15 1 10 1 3 C1 2 2 1 3 1 Z" fill="var(--orange)"/></svg>
      530-471-6328
    </li>
    <li>
      <svg viewBox="0 0 16 16" aria-hidden="true"><rect x="1" y="3" width="14" height="10" fill="var(--orange)"/><path d="M1 3 L8 9 L15 3" stroke="#000" stroke-width="1.3" fill="none"/></svg>
      info@gildedcritters.example
    </li>
    <li>
      <svg viewBox="0 0 16 16" aria-hidden="true"><g fill="none" stroke="var(--orange)" stroke-width="1.4"><circle cx="8" cy="8" r="6.5"/><ellipse cx="8" cy="8" rx="3" ry="6.5"/><path d="M1.5 8 H14.5 M2.5 4.8 H13.5 M2.5 11.2 H13.5"/></g></svg>
      <span>www.<span class="web-domain">gildedcritters.example</span></span>
    </li>
  </ul>

  <svg class="helix-band" viewBox="0 0 700 60" role="img" aria-label="Decorative double-helix strand in gold, orange and silver along the bottom edge">
    <path d="M0 60 L0 56 C120 36 230 50 350 42 C470 34 580 42 700 12 L700 60 Z" fill="url(#bandGradient)"/>
  </svg>
</section>

</body>
</html>
```